"Recently Leased" flyer for real estate agency

Looking to have a Recently Leased flyer designed. This will be delivered to apartments and houses closely situated to a property we have recently leased. The idea is to get the attention of owner/landlords in the area that may be considering leasing their property in the future and inform them of the great work we are doing locally. I would like the design to be a two sided flyer using the photoshop (PSD) template below (we would like to be able to edit this once complete should we need to update copy etc in the future). I would like the front page to look like our "for lease sign with the leased sticker on it and copy, I dont want it to look like a typical junk mail flyer.

Target Market(s)

Property owners and investors, male and female aged 28-70

Industry/Entity Type

Real Estate

Font styles to use
Sans Serif

Colors

Designer to choose colors to be used in the design.

Requirements
Must have
• Harbor Keystone Logo
• Contact information
• Copy supplied
Nice to have
• Slick, clean design,
Should not have
• too many colours or too busy a design.
• NO PROPERTY PHOTOS ON FRONT - I want this to be generic and not relate to a specific property image which might confuse people.

```html
<!DOCTYPE html>
<html lang="en">
<head>
<meta charset="utf-8">
<title>Harbor Keystone Agency – Recently Leased Flyer</title>
<link href="https://fonts.googleapis.com/css2?family=Open+Sans:wght@400;600;700&display=swap" rel="stylesheet">
<style>
  :root {
    --page-bg: #c6d8dc;
    --charcoal: #3e4348;
    --charcoal-deep: #2f3337;
    --teal: #1f7b87;
    --teal-light: #3097a2;
    --teal-accent: #3aa3ae;
    --sticker-red: #b5302e;
    --paper: #ededed;
    --white: #ffffff;
    --ink: #1c1c1c;
    --rule-dark: #111111;
  }
  * { box-sizing: border-box; margin: 0; padding: 0; }
  html, body { width: 1200px; height: 900px; overflow: hidden; }
  body {
    background: var(--page-bg);
    font-family: "Open Sans", Arial, sans-serif;
    position: relative;
  }
  .flyer {
    position: absolute;
    top: 74px;
    width: 341px;
    height: 724px;
    display: flex;
    flex-direction: column;
    background: var(--white);
  }
  .flyer--front { left: 205px; }
  .flyer--back { left: 662px; }
  .gap { height: 5px; background: var(--white); flex: none; }
  .gap--dark { background: var(--rule-dark); }

  .brand-header {
    height: 166px; background: var(--charcoal);
    display: flex; flex-direction: column; align-items: center; justify-content: center;
    color: #e6e6e6; font-weight: 600; text-align: center;
  }
  .brand-header .brand-name { font-size: 33px; letter-spacing: -0.5px; line-height: 1; }
  .brand-header .brand-sub { font-size: 12px; margin-top: 6px; letter-spacing: 1px; }

  .leased-band {
    height: 130px;
    background: radial-gradient(ellipse at 50% 40%, var(--teal-light), var(--teal) 75%);
    display: flex; align-items: center; justify-content: center;
  }
  .leased-sticker {
    transform: rotate(-3deg);
    background: var(--sticker-red);
    padding: 5px;
    box-shadow: 2px 4px 8px rgba(0,0,0,0.35);
  }
  .leased-sticker span {
    display: block;
    border: 3px solid var(--white);
    color: var(--white);
    font-size: 50px; font-weight: 400; line-height: 1;
    padding: 4px 20px 6px;
  }

  .intro {
    background: var(--charcoal);
    color: #f2f2f2;
    font-size: 11.2px; line-height: 1.22;
    text-align: justify; text-align-last: center;
    padding: 6px 18px;
    display: flex; flex-direction: column; justify-content: center;
  }
  .flyer--front .intro { height: 94px; }
  .flyer--back .intro { height: 52px; }
  .intro p + p { margin-top: 2px; }

  .benefits {
    background: radial-gradient(ellipse at 50% 35%, var(--teal-light), var(--teal) 80%);
    color: var(--white);
    list-style: none;
    display: flex; flex-direction: column; justify-content: center;
    font-size: 11.2px; line-height: 1.1;
  }
  .flyer--front .benefits { height: 180px; padding: 6px 24px 6px 50px; gap: 7px; }
  .flyer--back .benefits { height: 216px; padding: 6px 14px 6px 33px; gap: 8px; }
  .benefits li { position: relative; }
  .benefits li::before {
    content: ""; position: absolute; left: -18px; top: 4px;
    width: 5px; height: 5px; border-radius: 50%; background: var(--charcoal-deep);
  }

  .call-to-action {
    background: var(--paper); color: var(--ink);
    font-size: 11.6px; line-height: 1.2;
    text-align: justify; text-align-last: center;
    padding: 4px 18px;
    display: flex; align-items: center;
  }
  .flyer--front .call-to-action { height: 53px; }
  .flyer--back .call-to-action { height: 68px; }

  .contact {
    background: var(--charcoal); color: #f0f0f0;
    font-size: 11.2px; line-height: 1.25; text-align: center;
    display: flex; flex-direction: column; justify-content: center;
  }
  .flyer--front .contact { height: 57px; }
  .flyer--back .contact { height: 58px; }
  .contact .agent { color: var(--teal-accent); font-weight: 700; font-size: 15px; }
  .contact .sep { color: var(--teal-accent); margin: 0 6px; }

  .web-strip {
    background: var(--teal); color: #e8f4f5;
    font-size: 11.2px; text-align: center;
    display: flex; align-items: center; justify-content: center;
    flex: 1;
  }

  .photo { flex: none; }
  .photo--coast {
    height: 142px;
    background: linear-gradient(180deg, #6f9fbd 0%, #a8c3cf 35%, #8f8a6f 55%, #6f9fae 75%, #d9e6ea 100%);
  }
  .photo--home {
    height: 146px;
    background: linear-gradient(180deg, #8fb7d4 0%, #c9d6de 35%, #8a8a86 65%, #5d4a3c 100%);
  }
</style>
</head>
<body>

<section class="flyer flyer--front" aria-label="Flyer front">
  <header class="brand-header">
    <div class="brand-name">HARBOR KEYSTONE</div>
    <div class="brand-sub">AGENCY</div>
  </header>
  <div class="gap"></div>
  <div class="leased-band">
    <div class="leased-sticker"><span>LEASED!</span></div>
  </div>
  <div class="gap"></div>
  <div class="intro">
    <p>We recently leased a property in your building or street. Attracting a great reliable tenant and fantastic return for the owner.</p>
    <p>We received a high number of enquires and applications for this property and have a database of screened and qualified tenants looking to lease in your area.</p>
  </div>
  <div class="gap"></div>
  <ul class="benefits">
    <li>On average we lease properties 2 weeks faster than the Northern Beaches average</li>
    <li>Strong database of tenants actively looking in the area</li>
    <li>All we do is lease property, no sales – so tenanting and managing your property is our priority</li>
    <li>90 day money back guarantee on our level of service</li>
    <li>Highly competitive, simple all-inclusive pricing.</li>
    <li>Experience the difference of a property management specialist</li>
  </ul>
  <div class="gap gap--dark"></div>
  <div class="call-to-action">
    <p>Contact Sam to get your free rental appraisal or transfer your existing investment to an agency that will give it the attention it deserves and maxamise your return.</p>
  </div>
  <div class="contact">
    <div><span class="agent">SAM CARTER</span> Harbor Keystone Agency</div>
    <div>Level 2, 18 Marlowe St, Fernbay NSW 2090</div>
    <div>0400 555 218<span class="sep">|</span>sam@harborkeystone.com.au</div>
  </div>
  <div class="web-strip">www.harborkeystone.com.au</div>
</section>

<section class="flyer flyer--back" aria-label="Flyer back">
  <div class="photo photo--coast" role="img" aria-label="Coastal suburb with beach and headland homes"></div>
  <div class="gap"></div>
  <div class="photo photo--home" role="img" aria-label="Modern two-storey home with pool deck and lounges"></div>
  <div class="gap"></div>
  <div class="intro">
    <p>The fundamental idea behind Harbor Keystone Agency was to give landlords a simple and confidence inspiring experience. We achieve this through:</p>
  </div>
  <div class="gap"></div>
  <ul class="benefits">
    <li>Unique marketing that goes beyond the standard listing sites and has seen our average days-on-market at 5.9days for 2018.</li>
    <li>A simple, yet competitive fee structure.</li>
    <li>Excellent customer service through an experienced professional property manager.</li>
    <li>Sound advice and communication through out the leasing and management process.</li>
    <li>A simple yet powerful landlord portal which enables owners to view media rich inspection reports, financial reports and maintenance progress at anytime.</li>
    <li>We then back our service promise with a 90day money back guarantee.</li>
  </ul>
  <div class="gap gap--dark"></div>
  <div class="call-to-action">
    <p>If you have been considering leasing your property, purchasing a local investment or aren’t happy with your current managing agency, please don’t hesitate to contact your local rental specialist for more information:</p>
  </div>
  <div class="contact">
    <div><span class="agent">SAM CARTER</span> Harbor Keystone Agency</div>
    <div>Level 2, 18 Marlowe St, Fernbay NSW 2090</div>
    <div>0400 555 218<span class="sep">|</span>sam@harborkeystone.com.au</div>
  </div>
  <div class="web-strip">www.harborkeystone.com.au</div>
</section>

</body>
</html>
```